Cobalt Press website re-design

We would like to recreate the www.cobaltpress-demo.com.au website into a simpler and more sophisticated version. We want the buyer to be drawn to our site and establish that we are reputable and professional from the moment they enter. We want them to easily find the product or service they are looking for within our site, decide that they would like to find out more and either click through to obtain a quote or click through to contact a rep.

The current website has been created using MS Front Page, however we would like the newly designed site to be created in a mobile responsive WordPress CMS format

We are a Print Broker who can save clients time in hunting around for the right supplier for their print jobs. This is most likely appealing to larger organisations who haven’t got time to waste in finding quotes from many different suppliers for each type of job. We make it easy because we have access to a large network of trade only print & signage suppliers so we can select the best and most cost effective supplier depending on the type of print job. Further, because we don’t do the printing in-house we have low overheads which means we can ensure competitive prices.
Updates

Target Market(s)

Business owners, print managers, receptionists, marketing managers who are time poor, uneducated re:printing, after quick & cost effective solutions

Industry/Entity Type

Printing

Requirements
Must have
• Use the current logo and colours - see files uploaded
Limit scrolling and keep pages within view
Easy to see buttons that navigate the buyer through the site
The site is to be clear, easy to understand, free from clutter (ie.ensure white space) and have a Professional/corporate look
Easy to use Quotation forms
Imagery needs to be modern, and clean -see brightmarrow site

Competitor/other websites we like and why?
I like brightmarrow.com.au for its’ modern look. I like how the products are displayed in High resolution are very clean and uncluttered. You can easily find the product and access ‘get a quote’.
Pelham Print has a good layout for the quote request. Check out pelhamprint-demo.com.au
www.vendrak.com.au are print brokers/managers. Their descriptions are easy to understand but still heavy in content.
Nice to have
• 1. Home Page
½ page summary of the core business
Distinct buttons for products and services down the side (so that people can go straight to what they need.)
About Us (including profiles); Products and Services; Get a Quote; Contact us across the top

2. About Us
A brief overview of owner, staff and reps. Click through to Profiles for each region rep and contact details either as pop ups or separate pages.

3. Products and Services
Buttons or lists of products link to pop up with get a quote link within (this could be grouped such as Business Cards, Letterheads, Folders etc.; Club printing with plastic cards, sign in books, coasters etc.; Marketing such as flyers, posters, banners etc. (Note. look at how others have broken it up)
Include calling for advice for special products and finishes as service on how a job can be improved and done within budget.
4. Get a Quote
(2 sites mentioned below that I like for the get a quote system)

5. Contact Us
Clear sections divided by lines and details large starting with 1300 number
Head office
Regional numbers and areas they cover
Include emails.

Contact us now or click to request a rep contact you.

```html
<!DOCTYPE html>
<html lang="en">
<head>
<meta charset="utf-8">
<title>Cobalt Press — Home</title>
<link rel="stylesheet" href="https://fonts.googleapis.com/css2?family=Open+Sans:wght@300;400;600;700&family=Roboto+Condensed:wght@400;700&display=swap">
<style>
:root{
  --page-bg:#e9e9e9;
  --panel:#ffffff;
  --brand-red:#d81920;
  --brand-red-dark:#b40f15;
  --ink:#333333;
  --ink-soft:#555555;
  --line:#d6d6d6;
  --card-dark:#3f3f3f;
  --card-light:#efefef;
  --icon-grey:#9a9a9a;
  --dot:#c4c4c4;
}
*{box-sizing:border-box;margin:0;padding:0}
html,body{width:1200px;height:1004px;overflow:hidden}
body{background:var(--page-bg);font-family:"Open Sans",Arial,sans-serif;color:var(--ink);position:relative}
.site-panel{position:absolute;left:78px;top:25px;width:1024px;height:866px;background:var(--panel);border-radius:6px}
.brand{position:absolute;left:34px;top:36px;display:flex;align-items:center;gap:12px}
.brand-mark{width:64px;height:64px;background:var(--brand-red);border-radius:10px}
.brand-name{font-size:17px;letter-spacing:3px;color:#6a6a6a;font-weight:400;text-transform:uppercase;margin-top:28px}
.quote-btn{position:absolute;left:849px;top:29px;width:140px;height:38px;background:linear-gradient(#e8262c,var(--brand-red-dark));color:#fff;border-radius:4px;font-size:17px;display:flex;align-items:center;justify-content:center;box-shadow:0 2px 4px rgba(0,0,0,.25);text-decoration:none}
.call-line{position:absolute;right:35px;top:77px;font-size:24px;color:var(--ink);white-space:nowrap}
.main-nav{position:absolute;left:25px;top:120px;width:982px;height:56px;border:1px solid var(--line);border-bottom:none;border-radius:10px 10px 0 0;background:linear-gradient(#ffffff,#ececec);display:flex;align-items:center;padding-left:32px;padding-bottom:6px}
.main-nav a{font-size:16px;color:var(--ink);text-decoration:none;padding:0 17px;border-left:1px solid #bbb;line-height:18px}
.main-nav a:first-child{border-left:none;padding-left:0}
.hero{position:absolute;left:25px;top:170px;width:982px;height:329px;border:1px solid var(--line);border-radius:10px;background:#fff}
.hero-art{position:absolute;left:30px;top:22px;width:444px;height:284px;border-radius:8px;background:radial-gradient(ellipse at 50% 50%,#e2383d 0%,#c0161c 55%,#f6f6f6 80%)}
.hero-copy{position:absolute;left:531px;top:54px;width:430px}
.hero-kicker{font-size:26px;font-weight:300;color:var(--ink);line-height:34px;white-space:nowrap}
.hero-title{font-size:34px;font-weight:700;color:var(--ink);line-height:42px;letter-spacing:-.5px;white-space:nowrap}
.hero-text{font-size:12px;line-height:20px;color:var(--ink-soft);margin-top:6px}
.slider-dots{display:flex;gap:3px;margin-top:22px}
.slider-dots span{width:15px;height:15px;border-radius:50%;background:var(--dot)}
.services{position:absolute;left:25px;top:515px;display:flex;gap:23px}
.service-card{width:310px;height:149px;border-radius:8px;background:radial-gradient(circle at 50% 40%,#ffffff,var(--card-light));box-shadow:0 1px 3px rgba(0,0,0,.15);position:relative}
.service-card.is-active{background:var(--card-dark);width:308px}
.service-title{position:absolute;left:30px;top:19px;font-size:20px;font-weight:400;color:var(--ink);white-space:nowrap}
.is-active .service-title{color:#fff}
.service-icon{position:absolute;left:30px;top:54px;width:60px;height:60px}
.service-text{position:absolute;left:108px;top:51px;font-size:12px;line-height:20px;color:var(--ink-soft);white-space:nowrap}
.is-active .service-text{color:#e4e4e4}
.service-btn{position:absolute;left:108px;top:98px;width:87px;height:28px;background:linear-gradient(#4a4a4a,#262626);color:#fff;font-size:11px;border-radius:3px;display:flex;align-items:center;justify-content:center;text-transform:uppercase;border:1px solid #555}
.clients{position:absolute;left:31px;top:703px;width:970px;border-top:1px solid var(--line)}
.clients-head{height:41px;border-bottom:1px solid var(--line);display:flex;align-items:center;justify-content:space-between;padding-left:14px}
.clients-head h2{font-family:"Roboto Condensed","Arial Narrow",sans-serif;font-weight:700;font-size:20px;color:#4a4a4a;text-transform:uppercase}
.clients-arrows{width:38px;height:24px;background:#cfcfcf;display:flex;align-items:center;justify-content:center;gap:4px}
.clients-list{display:flex;justify-content:space-around;align-items:center;padding:0 22px;margin-top:34px}
.client-name{font-size:11px;font-weight:600;color:#6b6b6b;white-space:nowrap}
.site-footer{position:absolute;left:96px;top:913px;width:993px;height:32px}
.copyright{font-size:13px;color:#6a6a6a;position:absolute;left:0;top:4px;white-space:nowrap}
.social{position:absolute;right:0;top:0;display:flex;gap:3px}
.social span{width:31px;height:31px;border-radius:50%;background:#7a7a7a;display:block}
</style>
</head>
<body>
<div class="site-panel">
  <header>
    <div class="brand">
      <div class="brand-mark"></div>
      <div class="brand-name">Cobalt Press</div>
    </div>
    <a class="quote-btn" href="#">Free Quote</a>
    <div class="call-line">Call 1300 555 019</div>
  </header>
  <nav class="main-nav">
    <a href="#">Home</a><a href="#">About Us</a><a href="#">Products</a><a href="#">Contact Us</a><a href="#">Blog</a>
  </nav>
  <section class="hero">
    <div class="hero-art" role="img" aria-label="Three red guarantee badges: competitive pricing, quality, fast turnaround"></div>
    <div class="hero-copy">
      <p class="hero-kicker">Fast turnaround, Competitive pricing</p>
      <h1 class="hero-title">and quality guaranteed</h1>
      <p class="hero-text">Using Australia's leading print trade suppliers, we provide our clients with the most cost effective print solution in the market. We are constantly sourcing the most advanced technology in the industry to produce the lowest unit price, best quality and fastest Australia wide delivery.</p>
      <div class="slider-dots"><span></span><span></span><span></span><span></span></div>
    </div>
  </section>
  <section class="services">
    <div class="service-card is-active">
      <h3 class="service-title">Plastic Cards</h3>
      <svg class="service-icon" viewBox="0 0 60 60" fill="none" stroke="#9a9a9a" stroke-width="3">
        <rect x="4" y="14" width="52" height="38" rx="3"/><path d="M9 14V8h42v6M14 8V3h32v5"/>
        <circle cx="18" cy="29" r="4"/><path d="M11 43c1-6 13-6 14 0M31 27h18M31 34h18M31 41h12"/>
      </svg>
      <p class="service-text">Phasellus felis dolor, scelerisque<br>a, tempus eget, lobortis id</p>
      <div class="service-btn">Click here</div>
    </div>
    <div class="service-card">
      <h3 class="service-title">Offset Printing</h3>
      <svg class="service-icon" viewBox="0 0 60 60" fill="var(--icon-grey)">
        <rect x="15" y="4" width="30" height="14"/><rect x="2" y="20" width="56" height="22" rx="3"/>
        <rect x="13" y="34" width="34" height="22" fill="#fff" stroke="#9a9a9a" stroke-width="3"/>
        <path d="M19 42h22M19 48h22" stroke="#9a9a9a" stroke-width="3"/>
      </svg>
      <p class="service-text">Phasellus felis dolor, scelerisque<br>a, tempus eget, lobortis id</p>
      <div class="service-btn">Click here</div>
    </div>
    <div class="service-card">
      <h3 class="service-title">Digital Printing</h3>
      <svg class="service-icon" viewBox="0 0 60 60" fill="var(--icon-grey)">
        <path d="M8 2h30l16 16v40H8z"/><path d="M38 2v16h16" fill="#cfcfcf"/>
        <path d="M17 32h28M17 40h28M17 48h28" stroke="#fff" stroke-width="3"/>
      </svg>
      <p class="service-text">Phasellus felis dolor, scelerisque<br>a, tempus eget, lobortis id</p>
      <div class="service-btn">Click here</div>
    </div>
  </section>
  <section class="clients">
    <div class="clients-head">
      <h2>Our Corporate Clients</h2>
      <div class="clients-arrows">
        <svg width="10" height="10" viewBox="0 0 10 10"><path d="M8 0v10L0 5z" fill="#333"/></svg>
        <svg width="10" height="10" viewBox="0 0 10 10"><path d="M2 0v10l8-5z" fill="#333"/></svg>
      </div>
    </div>
    <div class="clients-list">
      <span class="client-name">Orchard Pop</span>
      <span class="client-name">KRN Group</span>
      <span class="client-name">Hillvale Club</span>
      <span class="client-name">Ember Grill</span>
      <span class="client-name">Yonder Mobile</span>
      <span class="client-name">Coastal Chook</span>
      <span class="client-name">Crumb &amp; Co</span>
      <span class="client-name">Bolt Hardware</span>
      <span class="client-name">Stacker Subs</span>
      <span class="client-name">Pine Depot</span>
    </div>
  </section>
</div>
<footer class="site-footer">
  <p class="copyright">Copyright © 2013 Company Name.&nbsp; All right reserved.&nbsp; Term of Use</p>
  <div class="social" aria-label="Social links"><span></span><span></span><span></span><span></span></div>
</footer>
</body>
</html>
```